Crime/mystery/thriller novel cover design

I am looking to get a cover designed for a novel. It is a crime/mystery/thriller set in Liverpool, England, between the 1970s and current day. I have permission to use some paintings by an artist for the cover, so it just needs put together and jazzed up. I am looking for something which has a fairly classic feel (so not just pulp airport thriller trash) but with some flair nonetheless.
The novel will be paperback, 127mm x 203mm with approx 18mm spine width. Can be gloss or matt cover, would be interesting to discuss.
The title is:
THE HARBOUR LANTERN
Author name:
GORDON T. VESELKA
Publisher:
BRIVOLTA PUBLISHING LTD (or simply BRIVOLTA)

I am still working on the back cover blurb but I will upload this when finished.
There are 4 images I could use for the cover though my favourite is the one called Dusk, Quayside Terraces.

```html
<!DOCTYPE html>
<html lang="en">
<head>
<meta charset="utf-8">
<title>The Harbour Lantern</title>
<link rel="stylesheet" href="https://fonts.googleapis.com/css2?family=Bebas+Neue&display=swap">
<style>
  :root {
    --sky-green: #1f3a34;
    --sky-teal: #3f6a62;
    --sky-amber: #d48a3e;
    --glow-gold: #e0b04a;
    --skyline-dark: #2a2233;
    --water-navy: #121a33;
    --reflection-rust: #8a4a2e;
    --deep-blue: #1a2452;
    --ink-white: #ffffff;
  }
  html, body {
    margin: 0;
    padding: 0;
    width: 751px;
    height: 1200px;
    overflow: hidden;
    background: var(--water-navy);
  }
  .cover {
    position: relative;
    width: 751px;
    height: 1200px;
    overflow: hidden;
    font-family: "Bebas Neue", "Oswald", sans-serif;
    color: var(--ink-white);
  }
  .cover-painting {
    position: absolute;
    inset: 0;
    background:
      linear-gradient(180deg,
        var(--sky-green) 0%,
        var(--sky-teal) 14%,
        var(--glow-gold) 26%,
        var(--sky-amber) 34%,
        var(--skyline-dark) 42%,
        #1e2a22 50%,
        #182038 60%,
        var(--water-navy) 68%,
        var(--reflection-rust) 76%,
        #5a3226 82%,
        var(--deep-blue) 88%,
        var(--water-navy) 100%);
  }
  .cover-shade {
    position: absolute;
    inset: 0;
    background: radial-gradient(ellipse at 50% 45%, rgba(0,0,0,0) 30%, rgba(0,0,0,0.35) 100%);
  }
  .author {
    position: absolute;
    top: 34px;
    left: 0;
    right: 0;
    text-align: center;
    font-size: 33px;
    letter-spacing: 21px;
    padding-left: 21px;
    line-height: 1;
  }
  .title {
    position: absolute;
    top: 530px;
    left: 0;
    right: 0;
    margin: 0;
    text-align: center;
    font-weight: 400;
    line-height: 1;
    text-shadow: 0 2px 10px rgba(0,0,0,0.45);
  }
  .title span { display: block; }
  .title-article {
    font-size: 47px;
    letter-spacing: 40px;
    padding-left: 40px;
  }
  .title-main {
    font-size: 186px;
    letter-spacing: 2px;
    margin-top: -4px;
    line-height: 0.86;
  }
  .title-sub {
    font-size: 80px;
    letter-spacing: 43px;
    padding-left: 43px;
    margin-top: 8px;
  }
  .publisher {
    position: absolute;
    right: 38px;
    bottom: 26px;
    font-size: 23px;
    letter-spacing: 6px;
    line-height: 1;
  }
</style>
</head>
<body>
  <div class="cover">
    <div class="cover-painting" role="img" aria-label="Painting: Dusk, Quayside Terraces — waterfront skyline under a swirling green and amber sky, reflected in dark blue water"></div>
    <div class="cover-shade"></div>

    <div class="author">GORDON T. VESELKA</div>

    <h1 class="title">
      <span class="title-article">THE</span>
      <span class="title-main">HARBOUR</span>
      <span class="title-sub">LANTERN</span>
    </h1>

    <div class="publisher">BRIVOLTA PUBLISHING LTD</div>
  </div>
</body>
</html>
```